Telecommunications/Power civil contractor needs business card design

Were a new telecommunications/power underground civil contractor that is looking for a new business card design. Our company colours are silver or grey and orange. Feel free to use the white background logo or the black background logo.

Target Market(s)

Local contractors, utility companies, private sector mining/energy companies, developers.

Industry/Entity Type

Telecommunications

Contact Information for Business Card

Each card will need the following info:
Persons name:
Title:
E-mail:
Phone number:
Shop Address:
Mailing Address:

Requirements
Must have
• Each card will need the following info:
• Persons name:
• Title:
• E-mail:
• Phone number:
• Shop Address:
• Mailing Address:

```html
<!DOCTYPE html>
<html lang="en">
<head>
<meta charset="utf-8">
<title>Ridgeline Contracting Inc – Business Card</title>
<link href="https://fonts.googleapis.com/css2?family=Montserrat:wght@700&family=Open+Sans:wght@400;600&display=swap" rel="stylesheet">
<style>
  :root{
    --orange:#f05a24;
    --grey-dark:#5e5f61;
    --grey-mid:#7a7b7d;
    --panel:#f0f0f0;
    --white:#ffffff;
    --stage:#cfd2d3;
  }
  *{box-sizing:border-box;margin:0;padding:0}
  html,body{width:1200px;height:900px;overflow:hidden}
  body{
    background:var(--stage);
    font-family:"Open Sans",Arial,sans-serif;
    display:flex;flex-direction:column;align-items:center;justify-content:center;gap:40px;
  }
  .card{
    width:560px;height:320px;position:relative;overflow:hidden;
    box-shadow:0 8px 24px rgba(0,0,0,.18);
  }
  /* Back face */
  .card-back{background:var(--orange);display:flex;align-items:center;justify-content:center}
  .back-brand{display:flex;align-items:center;gap:16px}
  .brand-circle{width:64px;height:64px;border:5px solid var(--white);border-radius:50%}
  .back-brand .brand-name{
    font-family:"Montserrat",Arial,sans-serif;font-weight:700;color:var(--white);
    font-size:26px;letter-spacing:1px;text-transform:uppercase;line-height:1.1
  }
  /* Front face */
  .card-front{background:var(--white)}
  .front-brand{position:absolute;left:34px;top:56px;width:220px;display:flex;flex-direction:column;align-items:center;gap:12px}
  .front-brand .brand-circle{width:58px;height:58px;border:4px solid var(--grey-dark)}
  .front-brand .brand-name{
    font-family:"Montserrat",Arial,sans-serif;font-weight:700;color:var(--grey-dark);
    font-size:20px;text-transform:uppercase;text-align:center;line-height:1.15
  }
  .contact-panel{
    position:absolute;right:22px;top:20px;width:270px;height:168px;
    background:var(--panel);padding:18px 22px;color:var(--grey-mid)
  }
  .person-name{color:var(--orange);font-size:22px;font-weight:400;line-height:1.1}
  .person-title{font-size:15px;margin:4px 0 14px}
  .contact-line{font-size:13px;line-height:1.5}
  .address-band{
    position:absolute;left:0;right:0;top:214px;height:68px;background:var(--orange);
    display:flex;align-items:center;padding:0 24px 0 110px;color:var(--white)
  }
  .address-lines{font-size:14px;line-height:1.45;flex:1}
  .pin-icon{position:absolute;left:34px;top:12px;width:30px;height:44px}
  .band-mark{width:34px;height:34px;border:3px solid var(--white);border-radius:50%}
</style>
</head>
<body>
  <section class="card card-back" aria-label="Card back">
    <div class="back-brand">
      <span class="brand-circle"></span>
      <span class="brand-name">Ridgeline<br>Contracting Inc</span>
    </div>
  </section>

  <section class="card card-front" aria-label="Card front">
    <div class="front-brand">
      <span class="brand-circle"></span>
      <span class="brand-name">Ridgeline<br>Contracting Inc</span>
    </div>
    <div class="contact-panel">
      <p class="person-name">John Doe</p>
      <p class="person-title">President</p>
      <p class="contact-line">123 456 789</p>
      <p class="contact-line">www.yourwebsite.com</p>
      <p class="contact-line">john@yoursite.com</p>
    </div>
    <div class="address-band">
      <svg class="pin-icon" viewBox="0 0 30 44" aria-hidden="true">
        <path d="M15 2C7.8 2 2 7.8 2 15c0 10 13 27 13 27s13-17 13-27C28 7.8 22.2 2 15 2z" fill="none" stroke="#fff" stroke-width="3"/>
        <circle cx="15" cy="15" r="5" fill="#fff"/>
      </svg>
      <div class="address-lines">
        <p>PO BOX 0004, Some place, AB 12345</p>
        <p>PO BOX 0001, location name, AB 12345</p>
      </div>
      <span class="band-mark"></span>
    </div>
  </section>
</body>
</html>
```